Contemporary Media Company with Logo Needs Business Card Design

Need a modern card design for a full service digital media company using the logo included. Also want the info below on the card. Probably list the services on the card back to save space for the front. Want something contemporary to impress prospective clients. You may want to submit both a somewhat more conservative design, and then a more wild one.
General Info: (this phrase need not be on the card)
Tod Parvin
Founder and CEO
949-628-4513
tod@lumavantstudio.example
lumavantstudio.example
Services: (this word need not be on the card)
Content & Experience Strategy
Brand Development
Search Engine Optimization
Website Design
Website Operation
Social Media Integration
Complete Video Solutions
Industry/Entity Type
Business
Contact Information for Business Card
Tod Parvin
Founder and CEO
949-628-4513
tod@lumavantstudio.example
lumavantstudio.example
Brand Development
Website Design
Website Operation
Social Media Integration
Complete Video Solutions
Look and feel

```html
<!DOCTYPE html>
<html lang="en">
<head>
<meta charset="utf-8">
<title>Lumavant Studio — Business Card</title>
<link href="https://fonts.googleapis.com/css2?family=Arimo:wght@400;700&display=swap" rel="stylesheet">
<style>
  :root {
    --page: #e8e5e0;
    --card-light: #f7f7f6;
    --card-dark: #2b2b2b;
    --orange: #f07a22;
    --amber: #f5b324;
    --grey-mark: #6f6f6f;
    --grey-text: #555555;
    --grey-soft: #9a9a9a;
    --line-dark: #4a4a4a;
  }
  * { box-sizing: border-box; margin: 0; padding: 0; }
  html, body { width: 1200px; height: 1023px; overflow: hidden; }
  body {
    background: var(--page);
    font-family: "Arimo", Arial, sans-serif;
    display: flex;
    align-items: center;
    justify-content: center;
    gap: 44px;
  }
  .card {
    width: 540px;
    height: 309px;
    border-radius: 3px;
    position: relative;
    box-shadow: 0 2px 6px rgba(0,0,0,0.12);
  }
  .card-front { background: var(--card-light); padding: 44px 46px; }
  .card-back { background: var(--card-dark); display: flex; flex-direction: column; align-items: center; justify-content: center; gap: 38px; }

  .brand { display: flex; align-items: center; gap: 14px; }
  .brand-square { width: 22px; height: 22px; background: var(--orange); }
  .brand-name {
    font-size: 34px;
    font-weight: 400;
    letter-spacing: 3px;
    text-transform: uppercase;
    color: var(--grey-mark);
  }
  .card-back .brand-name { color: #9d9d9d; }

  .person { margin-top: 34px; }
  .person-name { color: var(--orange); font-weight: 700; font-size: 20px; }
  .person-title { color: var(--grey-text); font-size: 15px; margin-top: 4px; }

  .divider { display: flex; height: 3px; width: 300px; margin: 14px 0 14px; }
  .divider span { display: block; height: 100%; }
  .divider .seg-amber { width: 14%; background: var(--amber); }
  .divider .seg-orange { width: 34%; background: var(--orange); }
  .divider .seg-grey { width: 28%; background: #c9c9c9; }
  .divider .seg-dark { width: 24%; background: var(--line-dark); }

  .contact-list { list-style: none; display: flex; flex-direction: column; gap: 7px; }
  .contact-item { display: flex; align-items: center; gap: 9px; color: var(--grey-text); font-size: 14px; }
  .contact-icon { width: 14px; height: 14px; flex: none; }

  .services {
    text-align: center;
    color: var(--grey-soft);
    font-size: 14px;
    line-height: 1.55;
  }
</style>
</head>
<body>
  <section class="card card-front" aria-label="Card front">
    <div class="brand">
      <span class="brand-square"></span>
      <span class="brand-name">Lumavant Studio</span>
    </div>
    <div class="person">
      <p class="person-name">Tod Parvin</p>
      <p class="person-title">Founder and CEO</p>
    </div>
    <div class="divider" aria-hidden="true">
      <span class="seg-amber"></span><span class="seg-orange"></span><span class="seg-grey"></span><span class="seg-dark"></span>
    </div>
    <ul class="contact-list">
      <li class="contact-item">
        <svg class="contact-icon" viewBox="0 0 14 14" aria-hidden="true"><rect width="14" height="14" rx="2" fill="#f07a22"/><path d="M4 3.5l1.6-.3.9 2-1 .8a5 5 0 0 0 2.5 2.5l.8-1 2 .9-.3 1.6c-3.6.2-6.7-2.9-6.5-6.5z" fill="#fff"/></svg>
        949-628-4513
      </li>
      <li class="contact-item">
        <svg class="contact-icon" viewBox="0 0 14 14" aria-hidden="true"><rect width="14" height="14" rx="2" fill="#f07a22"/><rect x="3" y="4.5" width="8" height="5.5" fill="none" stroke="#fff" stroke-width="1"/><path d="M3 4.5l4 3 4-3" fill="none" stroke="#fff" stroke-width="1"/></svg>
        tod@lumavantstudio.example
      </li>
      <li class="contact-item">
        <svg class="contact-icon" viewBox="0 0 14 14" aria-hidden="true"><rect width="14" height="14" rx="2" fill="#f07a22"/><circle cx="7" cy="7" r="3.8" fill="none" stroke="#fff" stroke-width="1"/><path d="M3.2 7h7.6M7 3.2c-2 2.2-2 5.4 0 7.6M7 3.2c2 2.2 2 5.4 0 7.6" fill="none" stroke="#fff" stroke-width=".8"/></svg>
        lumavantstudio.example
      </li>
    </ul>
  </section>

  <section class="card card-back" aria-label="Card back">
    <div class="brand">
      <span class="brand-square"></span>
      <span class="brand-name">Lumavant Studio</span>
    </div>
    <p class="services">
      Content &amp; Experience Strategy | Brand Development<br>
      Search Engine Optimization | Website Design | Website Operation<br>
      Social Media Integration | Complete Video Solutions
    </p>
  </section>
</body>
</html>
```